Postcard Design Harlow Bend D to D

Residential Real Estate, we want to implement a mail campaign in an specific geographic area.We want to include Market information on the area and statistics of the real estate market.This piece is going to be deliver via mail service door to door.

Target Market(s)

Home owners that might be interested in selling their houses

Industry/Entity Type

Real Estate

Font styles to use
Sans Serif

Colors
ec1f27
f78f20

Requirements
Must have
• Attractive look
• Include the information that we just sent to you
• Clear graphics and tables
• Must include clear information about our group

```html
<!DOCTYPE html>
<html lang="en">
<head>
<meta charset="utf-8">
<title>Harlow Bend Market Report Postcard</title>
<link href="https://fonts.googleapis.com/css2?family=Exo+2:ital,wght@0,600;1,700&family=Mulish:ital,wght@0,300;0,400;1,300;1,400;1,800&family=Patrick+Hand&display=swap" rel="stylesheet">
<style>
  :root {
    --red: #c8203a;
    --red-deep: #b51a31;
    --ink: #2f2f31;
    --gray: #6d6e71;
    --gray-light: #b9babc;
    --paper: #eeeeee;
    --white: #ffffff;
    --sky: #dfe6ea;
    --lawn: #9cbf6a;
  }
  * { box-sizing: border-box; margin: 0; padding: 0; }
  html, body { width: 1200px; height: 900px; overflow: hidden; background: #f2f2f2; }
  .postcard {
    position: relative; width: 1200px; height: 900px; overflow: hidden;
    background: var(--white); font-family: "Mulish", sans-serif; color: var(--ink);
  }
  .scene-photo {
    position: absolute; left: 0; top: 0; width: 1200px; height: 620px;
    background:
      linear-gradient(180deg, rgba(255,255,255,0) 0%, rgba(255,255,255,0) 55%, #ffffff 100%),
      linear-gradient(180deg, var(--sky) 0%, #c9ccc9 25%, #b8b7b0 45%, var(--lawn) 62%, #b9d294 80%);
  }
  .header-band {
    position: absolute; left: 0; top: 0; width: 1200px; height: 148px;
    background: rgba(255,255,255,0.86);
  }
  .title {
    position: absolute; left: 45px; top: 8px;
    font-family: "Exo 2", sans-serif; font-style: italic; font-weight: 700;
    font-size: 84px; line-height: 1; letter-spacing: -1px;
  }
  .title .accent { color: var(--red); }
  .title .rest { color: var(--gray); }
  .subtitle {
    position: absolute; left: 140px; top: 94px; width: 384px; text-align: right;
    font-family: "Exo 2", sans-serif; font-weight: 600; font-size: 36px; color: var(--gray);
  }
  .report-heading {
    position: absolute; left: 600px; top: 28px; width: 560px;
    font-weight: 400; font-size: 35px; line-height: 1.2; color: var(--ink);
  }
  .letter {
    position: absolute; left: 68px; top: 213px; width: 480px; height: 632px;
    background: var(--paper); transform: rotate(-4.5deg);
    box-shadow: 2px 4px 10px rgba(0,0,0,0.35);
    padding: 78px 40px 0 60px;
    font-family: "Patrick Hand", cursive; font-size: 18.5px; line-height: 1.05; color: #1c1c1c;
  }
  .letter p { margin-bottom: 22px; }
  .letter .salutation { font-size: 20px; margin-bottom: 24px; }
  .facts {
    position: absolute; left: 696px; top: 183px; width: 468px; height: 229px;
    background: rgba(255,255,255,0.88); border-radius: 12px; padding: 22px 32px 0 33px;
  }
  .facts h2 {
    text-align: center; color: var(--red); font-style: italic; font-weight: 800;
    font-size: 25px; margin-bottom: 16px;
  }
  .facts table { width: 100%; border-collapse: collapse; }
  .facts td {
    font-style: italic; font-weight: 300; font-size: 26.5px; line-height: 32px; color: var(--ink);
  }
  .facts td.value { text-align: right; }
  .quote {
    position: absolute; left: 700px; top: 432px; width: 470px; text-align: center;
    color: var(--red); font-style: italic; font-weight: 300; font-size: 31px; line-height: 1.22;
  }
  .divider { position: absolute; left: 735px; top: 602px; width: 430px; height: 2px; background: var(--gray-light); }
  .agent-photo {
    position: absolute; left: 552px; top: 603px; width: 232px; height: 297px;
    background: radial-gradient(ellipse at 50% 35%, #b88a72 0%, #7a4d3a 38%, #2a2a2d 70%, #1d1d20 100%);
    border-radius: 48% 48% 0 0 / 30% 30% 0 0; z-index: 3;
  }
  .group-name {
    position: absolute; left: 790px; top: 606px;
    font-weight: 300; font-size: 31px; color: var(--gray);
  }
  .group-name .tag {
    position: absolute; right: 28px; top: 34px; font-size: 11px; font-style: italic;
    color: var(--red); font-weight: 400; white-space: nowrap;
  }
  .agent {
    position: absolute; left: 790px; top: 665px; font-size: 25px; color: var(--red);
  }
  .agent .name { font-style: italic; font-weight: 800; }
  .agent .role { font-weight: 300; }
  .contact {
    position: absolute; top: 708px; font-style: italic; font-weight: 400;
    font-size: 14px; line-height: 19px; color: var(--ink);
  }
  .contact.phones { left: 790px; }
  .contact.address { left: 962px; }
  .brokerage {
    position: absolute; left: 796px; top: 775px; display: flex; align-items: center; gap: 7px;
    font-size: 15px; font-weight: 400; color: var(--gray); z-index: 2;
  }
  .brokerage .dot { width: 14px; height: 14px; border-radius: 50%; background: var(--red); }
  .badge {
    position: absolute; left: 944px; top: 760px; width: 54px; height: 54px;
    border-radius: 50%; background: #d7d8da; z-index: 2;
  }
  .footer-shapes { position: absolute; left: 0; top: 700px; width: 1200px; height: 200px; z-index: 1; }
  .website {
    position: absolute; left: 130px; top: 856px; z-index: 2;
    color: var(--white); font-style: italic; font-weight: 300; font-size: 27px;
  }
</style>
</head>
<body>
<main class="postcard">
  <div class="scene-photo" role="img" aria-label="Photo of a two-storey suburban house with trees and a green lawn"></div>

  <header class="header-band">
    <h1 class="title"><span class="accent">Harlow</span> <span class="rest">Bend</span></h1>
    <div class="subtitle">October Results 2015</div>
    <p class="report-heading">Market Report of single family sold and active homes</p>
  </header>

  <svg class="footer-shapes" viewBox="0 0 1200 200" aria-hidden="true">
    <path d="M0 140 C 300 120, 500 105, 700 90 L 1200 170 L 1200 200 L 0 200 Z" fill="none"/>
    <path d="M0 132 C 250 112, 480 98, 640 92 L 640 200 L 0 200 Z" fill="var(--red)"/>
    <path d="M0 118 C 250 100, 480 88, 640 84" stroke="var(--gray-light)" stroke-width="4" fill="none"/>
    <path d="M0 104 C 250 88, 480 78, 640 74" stroke="#d8d9db" stroke-width="2" fill="none"/>
    <path d="M780 200 C 950 150, 1080 160, 1200 175 L 1200 200 Z" fill="var(--red)"/>
    <path d="M760 185 C 940 120, 1080 120, 1200 130 L 1200 160 C 1060 150, 930 150, 780 200 Z" fill="#a7a8aa"/>
    <path d="M800 150 C 950 95, 1080 90, 1200 90" stroke="#cfd0d2" stroke-width="3" fill="none"/>
    <path d="M820 140 C 960 85, 1080 78, 1200 76" stroke="#e1e2e3" stroke-width="2" fill="none"/>
  </svg>

  <article class="letter">
    <p class="salutation">Dear Harlow Bend Neighbor:</p>
    <p>We expect that this information will be useful for you to learn about the Real estate market in your neighborhood.</p>
    <p>There are 28 properties “Active for Sale” on the market, with an average price of $303,589 USD and $101.06 USD per sf. Average time on market for sale 63 days.</p>
    <p>In process, “Pending to Close” are 9 houses at average price of $252,808 USD with a sale price of $103.11 per sf. with 34 Days on market.</p>
    <p>The past 6 Months market behavior was as follows: 97 Houses sold at average price of $263,545 with a sale price / sqf. of $100.50</p>
  </article>

  <section class="facts">
    <h2>Harlow Bend 2014 Facts</h2>
    <table>
      <tr><td>Single Family Properties</td><td class="value">1,667</td></tr>
      <tr><td>Median Square Feet</td><td class="value">2,568</td></tr>
      <tr><td>Median Lot Square Feet</td><td class="value">7,689</td></tr>
      <tr><td>Median Year Built</td><td class="value">2007</td></tr>
    </table>
  </section>

  <blockquote class="quote">“We will be glad to meet with you and have the opportunity to help you with your Real Estate requirements”</blockquote>

  <div class="divider"></div>
  <div class="agent-photo" role="img" aria-label="Portrait photo of the realtor"></div>

  <div class="group-name">The Marlowe Group<span class="tag">Real Estate</span></div>
  <div class="agent"><span class="name">Helena Marlowe</span> <span class="role">| Realtor</span></div>
  <div class="contact phones">C. 555 010 2841<br>O. 555 010 3907<br>E.helena@helenamarlowe.com</div>
  <div class="contact address">1820 Cedar Ridge Parkway<br>Fairbrook, TX 77001</div>

  <div class="brokerage"><span class="dot"></span>Brookline Realty</div>
  <div class="badge" aria-hidden="true"></div>

  <div class="website">www.themarlowegroup.com</div>
</main>
</body>
</html>
```